Structural Engineering Firm Looking for High-Impact Lead Generation Focused Design (for B2B)

A well-established structural engineering firm in the UK wants a new website designed for them which will help them realise more business from online. Directly through the website as well as Ads and lead platforms. They need to compare favourably to competitors and have clarity. Current Site is here: http://www.marlowgrantpartners.example/ - you can take imagery from this site if you want to help with the design.
Updates

Target Market(s)

Homeowners, Architects, Designers, Construction Companies and Landlords

Industry/Entity Type

Professional Services

Number of Pages Required

5+ page

Font styles to use
Sans Serif

Requirements
Must have
• A Strong, Simple and Professional Design with a Focus on Lead Generation
Nice to have
• Creativity in the Detail, Clear Messaging
Should not have
• Too Much Colour, Too 'Consumer', Too Much Variation

```html
<!DOCTYPE html>
<html lang="en">
<head>
<meta charset="utf-8">
<title>Marlow Grant Partners – Client Testimonials</title>
<link rel="stylesheet" href="https://fonts.googleapis.com/css2?family=Montserrat:wght@400;500;700&display=swap">
<style>
  :root {
    --accent: #f4e01c;
    --white: #ffffff;
    --page-bg: #232323;
    --divider: #3a3a3a;
    --card-bg: #333333;
    --card-text: #dcdcdc;
    --hero-dark: #3b3b3b;
    --hero-mid: #6d6a66;
    --hero-light: #9a958e;
    --avatar-a: #e08a1c;
    --avatar-b: #f1e6e0;
  }
  * { box-sizing: border-box; margin: 0; padding: 0; }
  html, body {
    width: 1200px;
    height: 830px;
    overflow: hidden;
    background: var(--page-bg);
    font-family: "Montserrat", sans-serif;
  }
  .site {
    position: relative;
    width: 1200px;
    height: 830px;
    background: var(--page-bg);
  }

  /* Hero slider */
  .hero {
    position: relative;
    height: 298px;
    overflow: hidden;
  }
  .hero-photo {
    position: absolute;
    inset: 0;
    background:
      linear-gradient(rgba(20,20,20,0.45), rgba(20,20,20,0.45)),
      linear-gradient(100deg, var(--hero-dark) 0%, var(--hero-light) 35%, var(--hero-mid) 60%, var(--hero-dark) 100%);
  }
  .hero-copy {
    position: absolute;
    top: 34px;
    left: 0;
    right: 0;
    text-align: center;
    color: var(--white);
    font-size: 22px;
    font-weight: 400;
    line-height: 58px;
  }
  .slider-dots {
    position: absolute;
    top: 220px;
    left: 0;
    right: 0;
    display: flex;
    justify-content: center;
    gap: 37px;
  }
  .slider-dot {
    width: 23px;
    height: 23px;
    border-radius: 50%;
    background: var(--white);
  }
  .slider-dot.is-active { background: var(--accent); }

  .hero-divider {
    height: 14px;
    background: var(--divider);
  }

  /* Testimonials */
  .testimonials {
    position: relative;
    height: 518px;
  }
  .section-title {
    position: absolute;
    top: 92px;
    left: 0;
    right: 0;
    text-align: center;
    color: var(--accent);
    font-size: 34px;
    font-weight: 700;
  }
  .testimonial-card {
    position: absolute;
    top: 262px;
    width: 523px;
    height: 206px;
    background: var(--card-bg);
  }
  .testimonial-card.client-one { left: 70px; }
  .testimonial-card.client-two { left: 621px; }
  .client-avatar {
    position: absolute;
    top: -52px;
    left: 1px;
    width: 104px;
    height: 104px;
    border-radius: 50%;
    border: 3px solid var(--white);
  }
  .client-one .client-avatar { background: var(--avatar-a); }
  .client-two .client-avatar { background: var(--avatar-b); }
  .quote-mark {
    position: absolute;
    top: 20px;
    right: 38px;
  }
  .testimonial-text {
    position: absolute;
    top: 72px;
    left: 30px;
    right: 30px;
    text-align: center;
    color: var(--card-text);
    font-size: 16px;
    line-height: 22px;
  }
</style>
</head>
<body>
<div class="site">
  <header class="hero">
    <div class="hero-photo" role="img" aria-label="Photograph of a bright modern dining room with a long table and black chairs"></div>
    <p class="hero-copy">1996. The Act dictates what a property owner, whether residential or commercial,<br>must do before commencing works on site.</p>
    <div class="slider-dots">
      <span class="slider-dot is-active"></span>
      <span class="slider-dot"></span>
      <span class="slider-dot is-active"></span>
      <span class="slider-dot"></span>
    </div>
  </header>
  <div class="hero-divider"></div>

  <section class="testimonials">
    <h2 class="section-title">From Our Great Clients</h2>

    <article class="testimonial-card client-one">
      <div class="client-avatar" role="img" aria-label="Illustrated portrait of a male client"></div>
      <svg class="quote-mark" width="38" height="12" viewBox="0 0 38 12" aria-hidden="true">
        <rect x="0" y="0" width="11" height="11" fill="var(--accent)"/>
        <rect x="26" y="0" width="11" height="11" fill="var(--accent)"/>
      </svg>
      <p class="testimonial-text">Lorem ipsum dolor sit amet, consectetur adipiscing elit, sed do eiusmod tempor incididunt ut labore..Lorem ipsum dolor sit amet, consectetur adipiscing elit, sed do eiusmod tempor incididunt ut labore</p>
    </article>

    <article class="testimonial-card client-two">
      <div class="client-avatar" role="img" aria-label="Illustrated portrait of a female client"></div>
      <svg class="quote-mark" width="38" height="12" viewBox="0 0 38 12" aria-hidden="true">
        <rect x="0" y="0" width="11" height="11" fill="var(--accent)"/>
        <rect x="26" y="0" width="11" height="11" fill="var(--accent)"/>
      </svg>
      <p class="testimonial-text">Lorem ipsum dolor sit amet, consectetur adipiscing elit, sed do eiusmod tempor incididunt ut labore..Lorem ipsum dolor sit amet, consectetur adipiscing elit, sed do eiusmod tempor incididunt ut labore</p>
    </article>
  </section>
</div>
</body>
</html>
```